Doctors clinic requires stationary designed

We require various types of stationary to be design based on the logo (attached). We require the following:
- Letterhead (A4 Portrait)
- Business Card (must include UV spot on rear)
- With compliments slip (DL Landscape)
- Appointments card (Folded A6)

We are a young clinical practice which boasts a modern and sophisticated approach to medicine so we require something which feels fresh and modern. Please include colours represented in the logo (contrasting teal and grey). We are calling for creative minds to put forth their ideas and we will be actively providing feedback on all designs.

thank you

```html
<!DOCTYPE html>
<html lang="en">
<head>
<meta charset="utf-8">
<title>Dr Clara Whitfield – Letterhead</title>
<link href="https://fonts.googleapis.com/css2?family=Source+Sans+3:wght@300;400;600&display=swap" rel="stylesheet">
<style>
  :root {
    --teal: #1f9e8f;
    --teal-light: #5fbfa9;
    --grey: #a3a3a3;
    --ink: #1a1a1a;
    --paper: #ffffff;
  }
  * { margin: 0; padding: 0; box-sizing: border-box; }
  html, body {
    width: 940px;
    height: 1200px;
    overflow: hidden;
    background: var(--paper);
  }
  .letterhead {
    position: relative;
    width: 940px;
    height: 1200px;
    background: var(--paper);
    font-family: "Source Sans 3", "Segoe UI", sans-serif;
  }
  .brand-dot {
    position: absolute;
    left: 104px;
    top: 67px;
    width: 56px;
    height: 56px;
    border-radius: 50%;
    background: var(--teal);
  }
  .brand-name {
    position: absolute;
    left: 210px;
    top: 70px;
    font-size: 38px;
    line-height: 48px;
    font-weight: 600;
    color: var(--teal);
    letter-spacing: -0.5px;
    white-space: nowrap;
  }
  .brand-divider {
    position: absolute;
    left: 495px;
    top: 66px;
    width: 1.5px;
    height: 60px;
    background: var(--teal);
  }
  .brand-role {
    position: absolute;
    left: 509px;
    top: 81px;
    font-size: 23px;
    line-height: 30px;
    font-weight: 600;
    color: var(--teal);
    white-space: nowrap;
  }
  .brand-role .joiner {
    font-weight: 300;
    color: var(--teal-light);
  }
  .footer {
    position: absolute;
    left: 36px;
    right: 32px;
    top: 1117px;
    font-size: 17px;
    line-height: 22px;
  }
  .footer-col { position: absolute; top: 0; white-space: nowrap; }
  .address { left: 0; }
  .address .venue { color: var(--grey); font-weight: 300; }
  .address .street { color: var(--ink); }
  .online { left: 453px; color: var(--teal-light); }
  .phones { left: 769px; color: var(--teal); }
  .footer-rule {
    position: absolute;
    left: 28px;
    width: 895px;
    top: 1165px;
    height: 4px;
    background: var(--teal);
  }
</style>
</head>
<body>
  <main class="letterhead">
    <header class="brand">
      <span class="brand-dot" aria-hidden="true"></span>
      <span class="brand-name">Dr Clara Whitfield</span>
      <span class="brand-divider" aria-hidden="true"></span>
      <span class="brand-role">Obstetrician <span class="joiner">and</span> Gynaecologist</span>
    </header>

    <footer class="footer">
      <div class="footer-col address">
        <p class="venue">Harbourside Private Hospital</p>
        <p class="street">Level 3 Harbour Clinic (North) Marlow Ave, Kingsbury</p>
      </div>
      <div class="footer-col online">
        <p>web: drclarawhitfield.com.au</p>
        <p>email: clara@drclarawhitfield.com.au</p>
      </div>
      <div class="footer-col phones">
        <p>Tel: 8125 3361</p>
        <p>Fax: 8125 3362</p>
      </div>
    </footer>
    <div class="footer-rule" aria-hidden="true"></div>
  </main>
</body>
</html>
```